Quivolt value proposition infographic

• Update to existing “Quivolt Features” wheel infographic (attached) to be more value proposition focused rather than feature focused.
• We want something fresh and new.
• Content messaging to be the 5 value prop points:
1. Intelligent Payment Capture
2. MultiSplit Payouts
3. Ultra Partnerships
4. NextGen Technology Platform
5. Unrivalled Geographical Coverage
• New artwork to appear on Quivolt assets –quivolt.com, business cards, proposal documents etc. – new artwork will need to be scalable.
• Layout is not locked into being a circle, but other design/layout elements of our website/brand should be considered when redesigning this artwork
• Guidelines and brand assets can be found here: https://www.quivolt.com/promotional-guidelines
• Deliverables: Visual file to use in online and offline marketing campaigns. File types: (in CYMK and/or RGB where applicable) .jpg, .png, EPS, PDF
• Tone and image: Functional, engaging, informative, energetic, accessible.
• We want our audience need to understand Quivolt’s total payment expertise focusing on the 5 points of value (listed below in ‘Messages’). They should want to seek more information on the Quivolt value drivers either through continued navigation through our website or contacting our team.

Target Market(s)

Companies searching for recurring payment proviers

Colors
0054AA
0677BA
7BADD7
CADEEF
E8F1F8
F0912C
F2A743
F7CA91
FBE8D2
FDF5EE

Requirements
Should not have
• The same design replacing the old wording with new words.

```html
<!DOCTYPE html>
<html lang="en">
<head>
<meta charset="utf-8">
<title>Quivolt Value Proposition</title>
<link href="https://fonts.googleapis.com/css2?family=Montserrat:wght@700&family=Outfit:wght@200;300;700&display=swap" rel="stylesheet">
<style>
  :root {
    --orange: #F28124;
    --orange-deep: #DA5A05;
    --navy: #383A50;
    --white: #FFFFFF;
    --ink: #1E1E24;
    --page: #FFFFFF;
  }
  html, body {
    margin: 0;
    padding: 0;
    width: 1200px;
    height: 1200px;
    overflow: hidden;
    background: var(--page);
  }
  .infographic {
    display: block;
    width: 1200px;
    height: 1200px;
  }
  .band-top { fill: var(--orange); }
  .panel { fill: var(--navy); }
  .hub-disc { fill: var(--white); stroke: var(--orange); stroke-width: 8; }
  .ring-orange { fill: none; stroke: var(--orange); stroke-width: 8; }
  .ring-white { fill: none; stroke: var(--white); stroke-width: 8; }
  .link-white { fill: none; stroke: var(--white); stroke-width: 7; }
  .link-orange { fill: none; stroke: var(--orange); stroke-width: 7; }
  .node-orange-ring { fill: var(--navy); stroke: var(--orange); stroke-width: 7; }
  .node-orange-dot { fill: var(--orange); }
  .node-white-ring { fill: var(--navy); stroke: var(--white); stroke-width: 8; }
  .node-white-dot { fill: var(--white); }
  .bubble-light { fill: var(--orange); }
  .bubble-deep { fill: var(--orange-deep); }
  .bubble-face { fill: var(--white); }
  .icon { fill: none; stroke: var(--ink); stroke-width: 2.6; stroke-linecap: round; stroke-linejoin: round; }
  .icon-fill { fill: var(--ink); }
  .icon-text { font-family: "Outfit", sans-serif; font-weight: 700; fill: var(--ink); text-anchor: middle; }
  .brand-name {
    font-family: "Outfit", sans-serif;
    font-weight: 700;
    font-size: 70px;
    letter-spacing: 3px;
    fill: var(--orange);
    text-anchor: middle;
  }
  .hub-title {
    font-family: "Outfit", sans-serif;
    font-weight: 200;
    font-size: 56px;
    fill: var(--navy);
    text-anchor: middle;
  }
  .label-strong {
    font-family: "Montserrat", sans-serif;
    font-weight: 700;
    font-size: 17px;
    fill: var(--white);
    text-anchor: middle;
  }
  .label-light {
    font-family: "Outfit", sans-serif;
    font-weight: 300;
    font-size: 18px;
    fill: var(--white);
    text-anchor: middle;
    letter-spacing: 0.5px;
  }
</style>
</head>
<body>
<svg class="infographic" viewBox="0 0 1932 1932" xmlns="http://www.w3.org/2000/svg" role="img" aria-label="Quivolt value proposition: five value points around a central hub">
  <!-- background -->
  <rect class="band-top" x="297" y="297" width="1337" height="250"/>
  <path class="panel" d="M297,546 H614 C700,430 830,362 966,362 C1102,362 1232,430 1316,546 H1634 V1634 H297 Z"/>

  <!-- hub outer segmented ring -->
  <path class="ring-orange" d="M712,808 A254,254 0 0 1 750.6,673.4"/>
  <path class="ring-white" d="M762,660 A254,254 0 0 1 884,572"/>
  <path class="ring-orange" d="M890,568 A254,254 0 0 1 1042,568"/>
  <path class="ring-white" d="M1048,572 A254,254 0 0 1 1170,660"/>
  <path class="ring-orange" d="M1175,667 A254,254 0 0 1 1220,808"/>

  <!-- connecting arc -->
  <path class="link-white" d="M679,905 A302,302 0 0 0 1252,905"/>
  <path class="link-orange" d="M679,905 A302,302 0 0 0 789,1056"/>
  <path class="link-orange" d="M1143,1056 A302,302 0 0 0 1252,905"/>

  <!-- hub -->
  <circle class="hub-disc" cx="966" cy="812" r="220"/>
  <text class="brand-name" x="966" y="762">QUIVOLT</text>
  <text class="hub-title" x="966" y="830">VALUE</text>
  <text class="hub-title" x="966" y="892">PROPOSITION</text>

  <!-- nodes -->
  <circle class="node-orange-ring" cx="679" cy="905" r="27"/>
  <circle class="node-orange-dot" cx="679" cy="905" r="14"/>
  <circle class="node-white-ring" cx="789" cy="1056" r="27"/>
  <circle class="node-white-dot" cx="789" cy="1056" r="14"/>
  <circle class="node-orange-ring" cx="966" cy="1113" r="27"/>
  <circle class="node-orange-dot" cx="966" cy="1113" r="14"/>
  <circle class="node-white-ring" cx="1143" cy="1056" r="27"/>
  <circle class="node-white-dot" cx="1143" cy="1056" r="14"/>
  <circle class="node-orange-ring" cx="1252" cy="905" r="27"/>
  <circle class="node-orange-dot" cx="1252" cy="905" r="14"/>

  <!-- value point 1: intelligent payment capture -->
  <g class="value-point">
    <polygon class="bubble-light" points="600,905 644,917 614,950"/>
    <circle class="bubble-light" cx="525" cy="955" r="96"/>
    <circle class="bubble-face" cx="525" cy="955" r="64"/>
    <g class="icon" transform="translate(525,955)">
      <circle r="20"/>
      <path d="M0,-28 V-20 M0,20 V28 M-28,0 H-20 M20,0 H28 M-20,-20 L-14,-14 M20,-20 L14,-14 M-20,20 L-14,14 M20,20 L14,14"/>
      <path d="M-36,-10 A38,38 0 0 1 -10,-36 M10,-36 A38,38 0 0 1 36,-10 M36,10 A38,38 0 0 1 10,36 M-10,36 A38,38 0 0 1 -36,10"/>
    </g>
    <text class="icon-text" x="525" y="963" font-size="22">$</text>
    <text class="label-strong" x="525" y="1086">INTELLIGENT</text>
    <text class="label-strong" x="525" y="1105">PAYMENT</text>
    <text class="label-light" x="525" y="1125">CAPTURE</text>
  </g>

  <!-- value point 2: multisplit payouts -->
  <g class="value-point">
    <polygon class="bubble-deep" points="728,1102 767,1086 762,1128"/>
    <circle class="bubble-deep" cx="693" cy="1187" r="96"/>
    <circle class="bubble-face" cx="693" cy="1187" r="64"/>
    <g class="icon" transform="translate(693,1187)">
      <circle r="20"/>
      <path d="M-6,-22 V-32 H-14 M6,-22 V-32 H14 M-6,22 V32 H-14 M6,22 V32 H14 M-22,-6 H-32 V-14 M-22,6 H-32 V14 M22,-6 H32 V-14 M22,6 H32 V14"/>
      <circle cx="-18" cy="-32" r="3.5"/><circle cx="18" cy="-32" r="3.5"/>
      <circle cx="-18" cy="32" r="3.5"/><circle cx="18" cy="32" r="3.5"/>
      <circle cx="-32" cy="-18" r="3.5"/><circle cx="-32" cy="18" r="3.5"/>
      <circle cx="32" cy="-18" r="3.5"/><circle cx="32" cy="18" r="3.5"/>
    </g>
    <text class="icon-text" x="693" y="1196" font-size="26">$</text>
    <text class="label-strong" x="693" y="1317">MULTISPLIT</text>
    <text class="label-light" x="693" y="1337">PAYOUTS</text>
  </g>

  <!-- value point 3: ultra partnerships -->
  <g class="value-point">
    <polygon class="bubble-light" points="946,1185 966,1151 986,1185"/>
    <circle class="bubble-light" cx="966" cy="1276" r="96"/>
    <circle class="bubble-face" cx="966" cy="1276" r="64"/>
    <g class="icon" transform="translate(966,1276)">
      <path d="M-36,4 A36,36 0 0 1 26,-26"/>
      <path d="M18,-34 L27,-26 L16,-20"/>
      <path d="M36,-4 A36,36 0 0 1 -26,26"/>
      <path d="M-18,34 L-27,26 L-16,20"/>
      <path d="M-20,-6 L-6,-12 L6,-6 L20,-12 M-18,-4 L-4,10 M-10,-2 L4,12 M-2,-2 L10,10 M6,-4 L14,4 M-6,-12 L10,2"/>
    </g>
    <text class="label-strong" x="966" y="1405">ULTRA</text>
    <text class="label-light" x="966" y="1425">PARTNERSHIPS</text>
  </g>

  <!-- value point 4: nextgen technology platform -->
  <g class="value-point">
    <polygon class="bubble-deep" points="1170,1128 1165,1086 1204,1102"/>
    <circle class="bubble-deep" cx="1238" cy="1187" r="96"/>
    <circle class="bubble-face" cx="1238" cy="1187" r="64"/>
    <g class="icon" transform="translate(1238,1187)">
      <path d="M-6,32 V2 A5,5 0 0 1 4,2 V14 M4,10 A4,4 0 0 1 12,10 V16 M12,12 A4,4 0 0 1 20,12 V26 A10,10 0 0 1 10,36 H-2 L-14,20 A4,4 0 0 1 -8,16 L-6,20"/>
      <path d="M-8,-10 C-16,-10 -16,-30 -30,-30 M8,-10 C16,-10 16,-30 30,-30 M-10,-4 H-28 M10,-4 H28 M-10,4 C-20,4 -20,14 -32,14 M24,14 H32"/>
      <circle cx="-34" cy="-30" r="3.5"/><circle cx="34" cy="-30" r="3.5"/>
      <circle cx="-32" cy="-4" r="3.5"/><circle cx="32" cy="-4" r="3.5"/>
      <circle cx="-36" cy="14" r="3.5"/><circle cx="36" cy="14" r="3.5"/>
      <circle cx="0" cy="-10" r="8"/>
    </g>
    <text class="label-strong" x="1238" y="1317">NEXTGEN</text>
    <text class="label-strong" x="1238" y="1336">TECHNOLOGY</text>
    <text class="label-light" x="1238" y="1356">PLATFORM</text>
  </g>

  <!-- value point 5: unrivalled geographical coverage -->
  <g class="value-point">
    <polygon class="bubble-light" points="1332,905 1288,917 1318,950"/>
    <circle class="bubble-light" cx="1406" cy="955" r="96"/>
    <circle class="bubble-face" cx="1406" cy="955" r="64"/>
    <g class="icon" transform="translate(1400,960)">
      <circle r="36"/>
      <ellipse rx="16" ry="36"/>
      <path d="M-36,0 H36 M-30,-18 H30 M-30,18 H30"/>
    </g>
    <g transform="translate(1436,926)">
      <path class="bubble-face" d="M0,22 L-11,6 A13,13 0 1 1 11,6 Z"/>
      <path class="icon" d="M0,22 L-11,6 A13,13 0 1 1 11,6 Z"/>
      <circle class="icon" cy="-4" r="4.5"/>
    </g>
    <text class="label-strong" x="1406" y="1086">UNRIVALLED</text>
    <text class="label-strong" x="1406" y="1105">GEOGRAPHICAL</text>
    <text class="label-light" x="1406" y="1125">COVERAGE</text>
  </g>
</svg>
</body>
</html>
```